Bikes for Dreams - Website Redesign

Create a professional website for a nonprofit; BikesforDreams.org
Please see bikesforelders.org and www.pedalsforhopes.org for the concept I am after.
The webpage should have a fun feel and should match the style of the company at www.pedalsforhopes.org. The pages to include are 'Home', 'About us' and 'Get Started'
Thank you and good luck!

```html
<!DOCTYPE html>
<html lang="en">
<head>
<meta charset="utf-8">
<title>Bikes for Dreams</title>
<link href="https://fonts.googleapis.com/css2?family=Roboto:ital,wght@0,400;0,500;0,700;1,400&family=Roboto+Condensed:wght@400;700&family=Open+Sans:wght@400;600&display=swap" rel="stylesheet">
<style>
:root{
  --navy:#0b2485;
  --red:#c4161c;
  --sky:#b9ddf4;
  --ink:#2b2b2b;
  --field:#c9c9c9;
  --footer:#f3f3f3;
  --white:#fff;
}
*{margin:0;padding:0;box-sizing:border-box}
html,body{width:1200px;height:3035px;overflow:hidden}
body{position:relative;font-family:'Roboto',sans-serif;color:var(--ink);background:var(--white)}
.abs{position:absolute}
.header{left:0;top:0;width:1200px;height:120px;background:var(--navy)}
.brand{left:100px;top:34px;display:flex;align-items:center;gap:12px;color:var(--white);font-family:'Roboto Condensed',sans-serif;font-weight:700;font-size:32px;text-transform:uppercase}
.brand-dot{width:34px;height:34px;border-radius:50%;background:var(--red)}
.hotline{right:96px;top:24px;display:flex;align-items:center;gap:10px;color:var(--white);font-size:18px}
.nav{left:587px;top:78px;display:flex;gap:30px;list-style:none;font-family:'Roboto Condensed',sans-serif;font-size:15px;color:var(--white)}
.nav li{padding-bottom:14px}
.nav .active{border-bottom:3px solid var(--red)}
.hero{left:0;top:120px;width:1200px;height:544px;background:linear-gradient(#cfe6f1 0%,#c4dde8 60%,#8cc15a 78%,#8f8f8f 85%,#777 100%)}
.hero-title{left:225px;top:244px;width:340px;text-align:center;font-family:'Roboto Condensed',sans-serif;color:#2a2a2a}
.hero-title h1{font-size:33px;font-weight:700;line-height:38px}
.hero-title p{font-size:23px;font-weight:700;line-height:28px}
.dots{left:560px;top:634px;display:flex;gap:6px}
.dots span{width:14px;height:14px;border-radius:50%;background:var(--white)}
.dots span:first-child{background:none;border:2px solid var(--white)}
.section-title{width:1200px;left:0;text-align:center;font-family:'Roboto Condensed',sans-serif;font-weight:700}
.how{top:757px;font-size:36px;color:var(--navy)}
.how em{font-style:normal;color:var(--red)}
.step{width:260px;text-align:center}
.step-icon{width:110px;height:110px;border-radius:50%;background:var(--red);margin:0 auto;display:flex;align-items:center;justify-content:center}
.step h3{margin-top:30px;font-family:'Roboto Condensed',sans-serif;font-size:22px;color:var(--red);font-weight:400}
.step p{margin-top:12px;font-size:12.5px;line-height:20px;color:#333}
.why{left:0;top:1190px;width:1200px;height:470px;background:var(--sky)}
.why-art{left:0;top:1190px;width:627px;height:470px;background:linear-gradient(#b9ddf4 0%,#9ab7c9 55%,#6f9a7f 72%,#cfcfcf 85%,#bdbdbd 100%)}
.why-copy{left:684px;top:1260px;width:440px}
.why-copy h2{font-family:'Roboto Condensed',sans-serif;font-size:34px;font-weight:400;color:#222;margin-bottom:22px}
.why-copy li{list-style:none;position:relative;padding-left:20px;font-size:11.5px;line-height:15px;margin-bottom:10px;color:#222}
.why-copy li::before{content:"";position:absolute;left:0;top:3px;width:9px;height:9px;border-radius:50%;background:#222}
.perks{left:0;top:1660px;width:1200px;height:192px;background:var(--navy)}
.perk{width:240px;text-align:center;color:var(--white);font-size:15px;font-weight:500}
.perk-icon{width:96px;height:96px;border:2px solid var(--white);border-radius:50%;margin:0 auto 22px;display:flex;align-items:center;justify-content:center}
.form-title{top:1932px;font-size:36px;font-weight:400;color:#222}
.form-sub{left:0;width:1200px;text-align:center;font-family:'Roboto Condensed',sans-serif;font-size:17px;color:var(--navy)}
.field{height:40px;border:1px solid var(--field);background:var(--white);font-style:italic;font-size:12px;color:#555;padding:12px 16px}
.submit{left:534px;top:2417px;width:132px;height:34px;background:var(--red);color:var(--white);font-size:14px;font-family:'Roboto Condensed',sans-serif;display:flex;align-items:center;justify-content:center;border-radius:2px}
.thanks{top:2504px;font-size:21px;font-weight:400;color:#333}
.help{left:250px;top:2546px;width:700px;text-align:center;font-size:15.5px;line-height:27px;color:#333}
.footer{left:0;top:2692px;width:1200px;height:287px;background:var(--footer)}
.f-col{top:2742px;font-family:'Open Sans',sans-serif;font-size:12.5px;color:#555}
.f-col h4{font-family:'Roboto Condensed',sans-serif;font-weight:400;font-size:18px;line-height:22px;color:#333;margin-bottom:20px}
.f-row{display:flex;gap:14px;margin-bottom:16px;line-height:20px;align-items:flex-start}
.f-row svg{margin-top:4px;flex:none}
.news p{width:250px;font-size:11.5px;line-height:19px;margin-bottom:14px}
.news .email{width:244px;height:40px;border:1px solid var(--field);background:var(--white);font-size:11px;padding:12px;color:#555}
.news .sub{margin-top:12px;width:120px;height:38px;background:var(--navy);color:var(--white);font-weight:600;font-size:12px;display:flex;align-items:center;justify-content:center}
.links li{list-style:none;font-size:11.5px;line-height:15px;margin-bottom:5px;padding-left:16px;position:relative}
.links li::before{content:"";position:absolute;left:0;top:4px;border-left:5px solid #444;border-top:4px solid transparent;border-bottom:4px solid transparent}
.social li{list-style:none;display:flex;align-items:center;gap:10px;margin-bottom:10px;font-size:14px}
.social span{width:26px;height:26px;border:1px solid #888;border-radius:50%}
.copyright{left:0;top:2979px;width:1200px;height:56px;border-top:1px solid #ddd;text-align:center;line-height:56px;font-size:12px;color:#555;font-family:'Open Sans',sans-serif}
</style>
</head>
<body>

<header class="abs header"></header>
<div class="abs brand"><span class="brand-dot"></span>Bikes for Dreams</div>
<div class="abs hotline">
  <svg width="30" height="30" viewBox="0 0 30 30"><circle cx="15" cy="15" r="13" fill="none" stroke="#fff" stroke-width="2"/><path d="M10 9c1-1 2-1 3 1l1 2c0 1-1 1-1 2 1 2 2 3 4 4 1 0 1-1 2-1l2 1c2 1 2 2 1 3-2 2-4 2-7 0-3-2-5-4-6-7-1-2 0-4 1-5z" fill="#fff"/></svg>
  Call toll-free 1-800-555-0147
</div>
<ul class="abs nav">
  <li class="active">HOME</li><li>ABOUT US</li><li>GET STARTED</li><li>HOW IT WORKS</li><li>FAQ</li><li>CONTACT</li>
</ul>

<div class="abs hero" role="img" aria-label="Illustration of a family beside their house waving as a pickup van carries away a donated bicycle in front of a city skyline"></div>
<div class="abs hero-title"><h1>DONATE BIKE TO CHARITY!</h1><p>Your bike can make a difference!</p></div>
<div class="abs dots"><span></span><span></span><span></span><span></span></div>

<h2 class="abs section-title how">HOW TO <em>DONATE</em></h2>

<div class="abs step" style="left:103px;top:866px">
  <div class="step-icon"><svg width="56" height="56" viewBox="0 0 56 56"><circle cx="28" cy="28" r="20" fill="none" stroke="#fff" stroke-width="3"/><text x="28" y="34" font-size="16" font-family="Roboto,sans-serif" font-weight="700" fill="#fff" text-anchor="middle">24</text></svg></div>
  <h3>CALL US</h3>
  <p>Sed ut perspiciatis unde omnis iste natus sit<br>voluptatem accusantium doloremque<br>laudantium, totam rem</p>
</div>
<div class="abs step" style="left:461px;top:866px">
  <div class="step-icon"><svg width="60" height="44" viewBox="0 0 60 44"><rect x="4" y="10" width="32" height="22" fill="#fff"/><path d="M36 16h10l8 8v8H36z" fill="#fff"/><circle cx="14" cy="36" r="5" fill="#fff"/><circle cx="46" cy="36" r="5" fill="#fff"/></svg></div>
  <h3>WE COLLECT IT</h3>
  <p>Sed ut perspiciatis unde omnis iste natus sit<br>voluptatem accusantium doloremque<br>laudantium, totam rem</p>
</div>
<div class="abs step" style="left:833px;top:866px">
  <div class="step-icon"><svg width="44" height="54" viewBox="0 0 44 54"><rect x="4" y="6" width="32" height="44" rx="3" fill="#fff"/><rect x="12" y="2" width="16" height="8" rx="2" fill="#fff" stroke="#c4161c" stroke-width="2"/><path d="M10 20h20M10 28h20M10 36h12" stroke="#c4161c" stroke-width="3"/></svg></div>
  <h3>TAX WRITE OFF</h3>
  <p>Sed ut perspiciatis unde omnis iste natus sit<br>voluptatem accusantium doloremque<br>laudantium, totam rem</p>
</div>
<svg class="abs" style="left:375px;top:908px" width="72" height="22" viewBox="0 0 72 22"><path d="M2 18Q34 0 64 10" fill="none" stroke="#0b2485" stroke-width="2" stroke-dasharray="5 4"/><path d="M60 4l8 7-10 3" fill="none" stroke="#0b2485" stroke-width="2"/></svg>
<svg class="abs" style="left:750px;top:926px" width="72" height="22" viewBox="0 0 72 22"><path d="M2 10Q34 22 64 10" fill="none" stroke="#0b2485" stroke-width="2" stroke-dasharray="5 4"/><path d="M58 5l8 5-8 6" fill="none" stroke="#0b2485" stroke-width="2"/></svg>

<section class="abs why"></section>
<div class="abs why-art" role="img" aria-label="Illustration of a happy family with two children and their bicycles in front of a blue house"></div>
<div class="abs why-copy">
  <h2>DONATE BIKE TO CHARITY!</h2>
  <ul>
    <li>Free Local Pickup: Rideable or not, Any Condition &amp; Pickup Anywhere.</li>
    <li>Fast Pickup: Same Day to 24 Hours.</li>
    <li>Income Tax Deduction: We issue you an IRS tax receipt &amp; offer the largest resale network to get you the highest tax write-off possible.</li>
    <li>No Paperwork Hassles: We take any bike and handle everything: receipts, transfer &amp; IRS paperwork.</li>
    <li>Bike donations help fund programs. And benefit Young Hopes Foundation. An IRS 501(c)3 nonprofit organization.</li>
  </ul>
</div>

<section class="abs perks"></section>
<div class="abs perk" style="left:157px;top:1693px">
  <div class="perk-icon"><svg width="44" height="40" viewBox="0 0 44 40"><path d="M22 38 4 20C-2 12 4 2 12 2c5 0 8 3 10 6 2-3 5-6 10-6 8 0 14 10 8 18z" fill="#fff"/></svg></div>Donation Accepted nationwide</div>
<div class="abs perk" style="left:392px;top:1693px">
  <div class="perk-icon"><svg width="42" height="42" viewBox="0 0 42 42"><rect x="4" y="6" width="26" height="32" fill="none" stroke="#fff" stroke-width="3"/><path d="M10 16h14M10 23h14M10 30h8" stroke="#fff" stroke-width="2.5"/><path d="M22 30 38 10" stroke="#fff" stroke-width="4"/></svg></div>Tax deductible</div>
<div class="abs perk" style="left:621px;top:1693px">
  <div class="perk-icon"><svg width="52" height="34" viewBox="0 0 52 34"><circle cx="11" cy="22" r="9" fill="none" stroke="#fff" stroke-width="3"/><circle cx="41" cy="22" r="9" fill="none" stroke="#fff" stroke-width="3"/><path d="M11 22 20 8h16l5 14M20 8l8 14h-17M36 8l-8 14M17 4h7" fill="none" stroke="#fff" stroke-width="3"/></svg></div>All Bike Types welcome</div>
<div class="abs perk" style="left:839px;top:1693px">
  <div class="perk-icon"><svg width="52" height="36" viewBox="0 0 52 36"><rect x="2" y="8" width="28" height="18" fill="#fff"/><path d="M30 12h10l8 8v6H30z" fill="#fff"/><circle cx="12" cy="29" r="4" fill="#fff"/><circle cx="40" cy="29" r="4" fill="#fff"/></svg></div>Pickup is free</div>

<h2 class="abs section-title form-title">DONATION PICK UP FORM</h2>
<div class="abs form-sub" style="top:2001px">CONTACT INFORMATION</div>
<div class="abs field" style="left:277px;top:2054px;width:314px">First Name:</div>
<div class="abs field" style="left:607px;top:2054px;width:316px">Last Name:</div>
<div class="abs field" style="left:277px;top:2107px;width:314px">Zip Code:</div>
<div class="abs field" style="left:607px;top:2107px;width:316px">Email Address:</div>
<div class="abs field" style="left:277px;top:2164px;width:646px">Day Phone:</div>
<div class="abs form-sub" style="top:2241px">BIKE DONATION INFORMATION</div>
<div class="abs field" style="left:277px;top:2295px;width:314px">Year of Bike:</div>
<div class="abs field" style="left:607px;top:2295px;width:316px">Make of Bike:</div>
<div class="abs field" style="left:277px;top:2348px;width:646px">Model of Bike:</div>
<div class="abs submit">SUBMIT NOW</div>
<h3 class="abs section-title thanks">THANK YOU FOR YOUR DONATION!</h3>
<p class="abs help">If you have any difficulty with this form or wish to speak with a representative immediately, then please call us toll-free at 1-800-555-0147.</p>

<footer class="abs footer"></footer>
<div class="abs f-col" style="left:97px">
  <h4>CONTACT US</h4>
  <div class="f-row"><svg width="12" height="16" viewBox="0 0 12 16"><path d="M6 15C2 10 1 8 1 6a5 5 0 0 1 10 0c0 2-1 4-5 9z" fill="none" stroke="#444" stroke-width="1.5"/><circle cx="6" cy="6" r="2" fill="#444"/></svg><div>Bikes for Dreams<br>420 Maple Ave, Springfield, OR 97477, USA</div></div>
  <div class="f-row"><svg width="12" height="14" viewBox="0 0 12 14"><path d="M2 1c1-1 2 0 3 2 0 1-1 1-1 2 1 2 2 3 4 4 1 0 1-1 2-1 2 1 3 2 2 3-2 2-5 1-8-2S0 3 2 1z" fill="#444"/></svg><div>Phone: 1-800-555-0147</div></div>
  <div class="f-row"><svg width="12" height="10" viewBox="0 0 12 10"><rect x="0.5" y="0.5" width="11" height="9" fill="#444"/><path d="M1 1l5 4 5-4" stroke="#fff" fill="none"/></svg><div>info@bikesfordreams.org</div></div>
</div>
<div class="abs f-col news" style="left:435px">
  <h4>SIGN UP FOR NEWSLETTER</h4>
  <p>Excepteur sint occaecat cupidatat non proident, sunt in culpa qui officia deserunt</p>
  <div class="email">Enter email</div>
  <div class="sub">SUBSCRIPTION</div>
</div>
<div class="abs f-col" style="left:767px">
  <h4>QUICK LINKS</h4>
  <ul class="links"><li>Home</li><li>About Us</li><li>Get Started</li><li>How It Works</li><li>Faq</li><li>Blog</li><li>Contact Us</li></ul>
</div>
<div class="abs f-col" style="left:1004px">
  <h4>SOCIAL</h4>
  <ul class="social"><li><span></span>Chatter</li><li><span></span>Snapline</li><li><span></span>Circles</li><li><span></span>Clipcast</li></ul>
</div>
<div class="abs copyright">©2017 Bikes for Dreams. All Rights Reserved.</div>

</body>
</html>
```